Business Card Design

New business card design

Target Market(s)

Residential & Commercial Property Managers

Industry/Entity Type

Plumbing Services

Contact Information for Business Card

Name - Owen Tredgold, title - Director, Phone Number - 0431 862 507, email - owen@rvb-plumbing.com.au, Company ABN - 73 215 904 386,

Font styles to use
Sans Serif

Colors
0054AA
0677BA
7BADD7
CADEEF
E8F1F8

```html
<!DOCTYPE html>
<html lang="en">
<head>
<meta charset="utf-8">
<title>RVB Plumbing Services – Business Card</title>
<link rel="stylesheet" href="https://fonts.googleapis.com/css2?family=Montserrat:wght@300;400&family=Poppins:wght@600&display=swap">
<style>
  :root {
    --page-bg: #e9e6e1;
    --card-dark: #121416;
    --card-mid: #3a3d41;
    --brand-deep: #0054AA;
    --brand-blue: #0677BA;
    --brand-sky: #7BADD7;
    --brand-mist: #CADEEF;
    --brand-ice: #E8F1F8;
    --text-silver: #d6d0c8;
    --text-soft: #cfc8c0;
  }
  * { margin: 0; padding: 0; box-sizing: border-box; }
  html, body { width: 1200px; height: 968px; overflow: hidden; }
  body {
    background: var(--page-bg);
    font-family: "Montserrat", Arial, sans-serif;
    position: relative;
  }
  .business-card {
    position: absolute;
    left: 100px; top: 207px;
    width: 1000px; height: 553px;
    border-radius: 28px;
    overflow: hidden;
    background: radial-gradient(ellipse 70% 90% at 30% 55%, var(--card-mid) 0%, #24272a 45%, var(--card-dark) 80%);
    box-shadow: 0 18px 40px rgba(0,0,0,0.25);
  }
  .feature-panel {
    position: absolute;
    right: 0; top: 0;
    width: 400px; height: 100%;
    background: linear-gradient(160deg, var(--brand-ice) 0%, var(--brand-mist) 30%, var(--brand-sky) 60%, var(--brand-blue) 100%);
    clip-path: polygon(30% 0, 100% 0, 100% 100%, 0 100%);
  }
  .company-name {
    position: absolute;
    left: 61px; top: 62px;
    font-weight: 300;
    font-size: 52px;
    letter-spacing: 4px;
    color: var(--text-silver);
    line-height: 1;
  }
  .company-tagline {
    position: absolute;
    left: 61px; top: 128px;
    font-weight: 300;
    font-size: 52px;
    letter-spacing: 4px;
    color: var(--text-silver);
    line-height: 1;
  }
  .person-name {
    position: absolute;
    left: 60px; top: 283px;
    font-family: "Poppins", Arial, sans-serif;
    font-weight: 600;
    font-size: 35px;
    color: var(--brand-blue);
    line-height: 1.2;
  }
  .person-title {
    position: absolute;
    left: 61px; top: 331px;
    font-size: 25px;
    color: var(--text-soft);
  }
  .contact-list { position: absolute; left: 61px; top: 384px; list-style: none; }
  .contact-item {
    display: flex; align-items: center; gap: 18px;
    font-size: 25px; color: var(--text-soft);
    height: 35px;
  }
  .contact-icon { width: 25px; height: 25px; fill: var(--brand-blue); }
  .company-abn {
    position: absolute;
    left: 61px; top: 484px;
    font-size: 25px;
    color: var(--text-soft);
  }
</style>
</head>
<body>
  <div class="business-card">
    <div class="feature-panel" role="img" aria-label="Large blue brand decoration area"></div>
    <div class="company-name">RVB</div>
    <div class="company-tagline" style="top:128px;font-size:20px;letter-spacing:14px;">plumbing services</div>
    <div class="person-name">Owen Tredgold</div>
    <div class="person-title">Director</div>
    <ul class="contact-list">
      <li class="contact-item">
        <svg class="contact-icon" viewBox="0 0 24 24" aria-hidden="true"><path d="M6.6 10.8c1.4 2.8 3.8 5.1 6.6 6.6l2.2-2.2c.3-.3.7-.4 1-.2 1.1.4 2.3.6 3.6.6.6 0 1 .4 1 1V20c0 .6-.4 1-1 1C10.6 21 3 13.4 3 4c0-.6.4-1 1-1h3.5c.6 0 1 .4 1 1 0 1.3.2 2.5.6 3.6.1.3 0 .7-.2 1z"/></svg>
        <span>0431 862 507</span>
      </li>
      <li class="contact-item">
        <svg class="contact-icon" viewBox="0 0 24 24" aria-hidden="true"><path d="M2 5h20v14H2z M2 5l10 8 10-8" fill="var(--brand-blue)" stroke="var(--card-dark)" stroke-width="1.5"/></svg>
        <span>owen@rvb-plumbing.com.au</span>
      </li>
    </ul>
    <div class="company-abn">ABN - 73 215 904 386</div>
  </div>
</body>
</html>
```